Nutrigenomics Business card design

Nutrigenomics is an exciting emerging field where I sequence the DNA from a saliva swab and then tailor a personalised nutritional program according to the persons genetics. It is possible to turn down undesirable genes that may be stuck "on" all the time causing inflammation etc. Equally important we switch "on" genes that might be stuck "off" as is often the case with autism. A large portion of my clients are autistic children. We see huge changes in functionality with the appropriate changes in diet to regulate their gene expression. This technology is definitely the way of the future.
I need a logo that will clearly show the combination of genetics with nutrition. The word "Nutrigenomics" still isn't in common use yet. I'm thinking maybe a DNA helix - (I think most people associate a helix with DNA or genes, but I'm open to suggestions) Combined somehow with food - preferably vegetables/ fruit/ meat/eggs etc. Definitely not grains or dairy - we take autistic kids off those 2 food groups straight away.
Green in it somewhere? I somehow associates healthy living / whole foods nutrition with the colour green. You guys know more about colours than me :-)
Maybe a helix could morph into a body shape filled with foods (along the lines of "you are what you eat" or something...)

Target Market(s)

The majority of my clients to date are people in their 40's wanting to improve their health or their children's health.

Industry/Entity Type

Nutrition

Contact Information for Business Card

Front of card:
Dr Moira Pellton (B App Sci, PhD Molecular Pathology)
Certified Vitacorde Practitioner and RUNE Nutritionist
52 Tallowby Rd, Tallowby
0417386254
dr.moirapellton@quillmail.com
drmoirapellton.com.au
Back of card:
Small Photo of me, Dr Moira Pellton
Specialises in Autism, ADHD, Fussy Eaters, Gut Issues, Food Intolerances, Healthy Ageing

Logo Text

Dr Moira Pellton

Logo styles of interest
Pictorial/Combination Logo
Character Logo
Requirements
Must have
• A logo showing a clear link between genes and nutrition
The box for what I want written on the card is not coming up when I try to edit so I'll put it here....
Front of card:
Dr Moira Pellton
(B App Sci, PhD Molecular Pathology) in smaller writing under my name

Certified Nutrigenomist
Certified RUNE Nutritionist

then use your nice symbols for the address, ph etc as below

52 Tallowby Rd, Tallowby
0417386254
dr.moirapellton@quillmail.com
www.drmoirapellton.com.au

Back of card:
Small Photo of me
Dr Moira Pellton
Specialises in:
Nutrigenomics
Healthy Ageing
Autism / ADHD
Gut Issues
Food Intolerances
Should not have
• No bread or grains of any sort
No dairy - milk cheese etc

```html
<!DOCTYPE html>
<html lang="en">
<head>
<meta charset="utf-8">
<title>Dr Moira Pellton – Business Card</title>
<link rel="stylesheet" href="https://fonts.googleapis.com/css2?family=Arimo:ital,wght@0,400;0,700;1,400&display=swap">
<style>
  :root {
    --green: #3aa935;
    --green-dark: #248a22;
    --green-light: #7cc95a;
    --ink: #222222;
    --paper: #ffffff;
    --backdrop: #e9ece8;
    --photo-warm: #b9785a;
    --photo-dark: #3a2620;
    --art-green: #8fcf6a;
    --art-warm: #f2b85a;
  }
  * { margin: 0; padding: 0; box-sizing: border-box; }
  html, body {
    width: 1200px; height: 900px; overflow: hidden;
    background: var(--backdrop);
    font-family: "Arimo", Arial, sans-serif;
  }
  .canvas { position: relative; width: 1200px; height: 900px; }
  .card {
    position: absolute; width: 665px; height: 380px;
    background: var(--paper);
    box-shadow: 0 6px 18px rgba(0,0,0,0.18);
    overflow: hidden;
  }
  .card svg.card-shapes { position: absolute; inset: 0; }

  /* Back of card */
  .card--back { left: 120px; top: 50px; }
  .back-name {
    position: absolute; left: 302px; top: 36px; width: 200px;
    text-align: center; white-space: nowrap;
    color: var(--green); font-weight: 700; font-size: 23px;
  }
  .portrait {
    position: absolute; left: 345px; top: 76px; width: 158px; height: 136px;
    background: radial-gradient(circle at 50% 55%, var(--photo-warm) 0%, var(--photo-dark) 85%);
  }
  .specialties { position: absolute; left: 36px; top: 104px; color: var(--green); }
  .specialties-title { font-size: 19px; margin-bottom: 6px; }
  .specialties ul { list-style: none; margin-left: 6px; }
  .specialties li { font-size: 21px; line-height: 27px; padding-left: 28px; position: relative; }
  .specialties li::before {
    content: ""; position: absolute; left: 0; top: 8px;
    width: 12px; height: 12px; border-radius: 50%; background: var(--green);
  }

  /* Front of card */
  .card--front { left: 415px; top: 470px; }
  .name-banner {
    position: absolute; left: 0; top: 0;
    color: #fff; font-size: 27px; padding: 22px 0 0 28px; white-space: nowrap;
  }
  .credentials { position: absolute; left: 28px; top: 72px; color: var(--green); }
  .degree { font-size: 15px; margin-bottom: 12px; }
  .certification { font-size: 15px; font-style: italic; line-height: 19px; }
  .contact-list { position: absolute; left: 22px; top: 172px; list-style: none; color: var(--ink); }
  .contact-list li { display: flex; align-items: center; gap: 9px; font-size: 16px; line-height: 23px; }
  .contact-list svg { width: 15px; height: 15px; flex: none; }
  .logo-art {
    position: absolute; left: 400px; top: 78px; width: 240px; height: 250px;
    background:
      radial-gradient(ellipse at 50% 85%, var(--art-warm) 0%, rgba(242,184,90,0) 55%),
      radial-gradient(ellipse at 50% 40%, var(--art-green) 0%, rgba(143,207,106,0) 70%);
    opacity: 0.85;
  }
</style>
</head>
<body>
<main class="canvas">

  <section class="card card--back" aria-label="Back of business card">
    <svg class="card-shapes" width="665" height="380" viewBox="0 0 665 380" aria-hidden="true">
      <path d="M540 0 C 665 80, 665 290, 380 380 L665 380 L665 0 Z" fill="var(--green)"/>
      <path d="M515 0 C 655 80, 655 285, 340 380 L380 380 C 665 290, 665 80, 540 0 Z" fill="var(--green-light)"/>
      <path d="M526 0 C 660 80, 660 288, 360 380" fill="none" stroke="#fff" stroke-width="6"/>
      <path d="M290 118 C 302 160, 302 200, 290 242" fill="none" stroke="var(--green)" stroke-width="3"/>
    </svg>
    <h2 class="back-name">Dr Moira Pellton</h2>
    <div class="portrait" role="img" aria-label="Small portrait photo of Dr Moira Pellton"></div>
    <div class="specialties">
      <p class="specialties-title">Specialises in:</p>
      <ul>
        <li>Autism</li>
        <li>ADHD</li>
        <li>Fussy Eaters</li>
        <li>Gut Issues</li>
        <li>Food Intolerances</li>
        <li>Healthy Ageing</li>
      </ul>
    </div>
  </section>

  <section class="card card--front" aria-label="Front of business card">
    <svg class="card-shapes" width="665" height="380" viewBox="0 0 665 380" aria-hidden="true">
      <polygon points="0,14 395,14 372,62 0,62" fill="var(--green)"/>
      <path d="M0 262 C 180 320, 430 345, 665 330 L665 380 L0 380 Z" fill="var(--green)"/>
      <path d="M0 250 C 180 310, 430 335, 665 320" fill="none" stroke="var(--green-light)" stroke-width="2"/>
    </svg>
    <h1 class="name-banner">Dr Moira Pellton</h1>
    <div class="credentials">
      <p class="degree">B App Sci - PhD Molecular Pathology</p>
      <p class="certification">Certified Nutrigenomist</p>
      <p class="certification">Certified RUNE Nutritionist</p>
    </div>
    <ul class="contact-list">
      <li>
        <svg viewBox="0 0 16 16" aria-hidden="true"><path d="M8 1 L15 7.5 H13 V15 H9.5 V10.5 H6.5 V15 H3 V7.5 H1 Z" fill="var(--green)"/></svg>
        52 Tallowby Rd, Tallowby
      </li>
      <li>
        <svg viewBox="0 0 16 16" aria-hidden="true"><rect x="1" y="6" width="14" height="9" rx="2" fill="var(--green)"/><path d="M2 6 C2 1, 14 1, 14 6 L11 6 L11 4 L5 4 L5 6 Z" fill="var(--green)"/><circle cx="8" cy="10.5" r="2.2" fill="#fff"/></svg>
        0417 386 254
      </li>
      <li>
        <svg viewBox="0 0 16 16" aria-hidden="true"><rect x="1" y="3" width="14" height="10" fill="var(--green)"/><path d="M1 3 L8 9 L15 3" fill="none" stroke="#fff" stroke-width="1.4"/></svg>
        dr.moirapellton@quillmail.com
      </li>
      <li>
        <svg viewBox="0 0 16 16" aria-hidden="true"><circle cx="8" cy="8" r="7" fill="var(--green)"/><path d="M1 8 H15 M8 1 C4 5, 4 11, 8 15 M8 1 C12 5, 12 11, 8 15" fill="none" stroke="#fff" stroke-width="1"/></svg>
        drmoirapellton.com.au
      </li>
    </ul>
    <div class="logo-art" role="img" aria-label="Logo illustration: a body outline formed by a DNA helix rising from fresh fruit and vegetables"></div>
  </section>

</main>
</body>
</html>
```